Crafted Ember Website

Would like a website designed for my fitness and nutrition coaching company Craft Ember. I have a company logo and would like to keep the page layout clean and simple. Needs to look great on computer and mobile devices.

Target Market(s)

Target market is individuals looking to make changes in their health and nutrition with the help of an online coach.

Industry/Entity Type

Fitness

Number of Pages Required

2 page

Colors
3176b5
0355a3
85acd3
cedeed
f8fcfd
ffffff

Requirements
Must have
• The first page should have the company logo and name towards the top and below that client before and after photos scrolling or displaying in some manner. Also would like a section that states services offered and a section about myself since I am the primary coach for clients.

```html
<!DOCTYPE html>
<html lang="en">
<head>
<meta charset="utf-8">
<title>Crafted Ember — Fitness &amp; Nutrition Coaching</title>
<link rel="stylesheet" href="https://fonts.googleapis.com/css2?family=Open+Sans:wght@400;600;700&family=Montserrat:wght@400;600;700;800&display=swap">
<style>
:root{
  --blue:#3176b5;
  --blue-deep:#0355a3;
  --blue-night:#0a3f78;
  --blue-soft:#85acd3;
  --blue-pale:#cedeed;
  --snow:#f8fcfd;
  --white:#ffffff;
  --ink:#3d3f45;
  --grey:#6b6e75;
  --line:#d9dde3;
  --coach-bg:#e4e5ea;
  --dark-btn:#2b2d33;
}
*{margin:0;padding:0;box-sizing:border-box}
html,body{width:1200px;height:3008px;overflow:hidden;background:var(--white)}
body{position:relative;font-family:"Open Sans",Arial,sans-serif;color:var(--ink)}
.abs{position:absolute}

/* top utility bar */
.utility{left:0;top:0;width:1200px;height:40px;background:var(--white);border-bottom:1px solid var(--line)}
.social{left:120px;top:10px;display:flex;gap:8px}
.social span{width:20px;height:20px;border-radius:50%;background:var(--blue)}
.contact-item{top:11px;font-size:13px;color:var(--grey);display:flex;align-items:center;gap:6px}
.contact-item svg{width:14px;height:14px;fill:var(--blue)}
.join-top{left:940px;top:6px;width:110px;height:28px;background:var(--dark-btn);color:var(--white);font:600 12px "Montserrat",sans-serif;display:flex;align-items:center;justify-content:center;letter-spacing:.5px}

/* header */
.brand{left:120px;top:48px;width:150px;text-align:center}
.brand-mark{width:46px;height:46px;background:var(--blue);margin:0 auto 6px}
.brand-name{font:800 18px "Montserrat",sans-serif;color:var(--blue-deep);letter-spacing:.5px}
.nav{left:390px;top:66px;display:flex;gap:6px}
.nav a{font:600 13px "Montserrat",sans-serif;color:var(--ink);text-decoration:none;padding:8px 14px;letter-spacing:.5px}
.nav a.current{border:1px solid var(--blue);border-radius:4px;color:var(--blue-deep)}

/* hero */
.hero-photo{left:0;top:144px;width:1200px;height:676px;background:linear-gradient(120deg,#c9ccd3 0%,#9ea7b5 40%,#5c6a80 75%,#3c4658 100%)}
.hero-square{left:525px;top:740px;width:150px;height:150px;background:var(--blue);border:8px solid var(--white)}

/* welcome */
.welcome{left:0;top:955px;width:1200px;text-align:center}
.welcome-kicker{font:600 22px "Montserrat",sans-serif;color:var(--grey);letter-spacing:1px}
.welcome-title{font:800 66px "Montserrat",sans-serif;color:var(--blue-deep);letter-spacing:1px;margin-top:6px;line-height:1.1}
.welcome-copy{width:760px;margin:22px auto 0;font-size:15px;line-height:1.6;color:var(--grey)}
.btn{display:inline-flex;align-items:center;justify-content:center;background:var(--blue);color:var(--white);font:700 18px "Montserrat",sans-serif;border-radius:8px;letter-spacing:.5px}
.join-hero{left:528px;top:1192px;width:144px;height:54px}

/* success story */
.story{left:0;top:1312px;width:1200px;height:508px;background:linear-gradient(100deg,var(--blue-night) 0%,var(--blue-deep) 55%,#0b4c92 100%)}
.story-name{left:120px;top:1392px;font:800 42px "Montserrat",sans-serif;color:var(--white)}
.story-sub{left:120px;top:1446px;font:600 28px "Montserrat",sans-serif;color:var(--white)}
.story-copy{left:120px;top:1500px;width:360px;font-size:15px;line-height:1.6;color:var(--blue-pale)}
.story-result{left:120px;top:1610px;font-size:14px;font-weight:700;color:var(--white)}
.read-more{left:120px;top:1690px;width:110px;height:40px;font-size:15px;border-radius:6px;background:var(--blue)}
.label-ba{font:600 26px "Montserrat",sans-serif;color:var(--white)}
.ba-frame{top:1392px;width:236px;height:240px;border:6px solid var(--white);background:linear-gradient(180deg,#b98f76 0%,#8c6350 100%)}
.ba-weight{top:1648px;width:236px;text-align:center;font-size:24px;color:var(--blue-pale)}

/* services */
.services-title{left:0;top:1878px;width:1200px;text-align:center;font:700 38px "Montserrat",sans-serif;color:var(--blue-deep)}
.services-sub{left:0;top:1936px;width:1200px;text-align:center;font-size:15px;color:var(--grey)}
.service{top:1992px;width:228px}
.service-photo{height:134px}
.service-label{height:32px;background:var(--blue);color:var(--white);font:700 13px "Montserrat",sans-serif;display:flex;align-items:center;justify-content:center;letter-spacing:.5px}

/* coach */
.coach{left:0;top:2248px;width:1200px;height:472px;background:var(--coach-bg)}
.coach-photo{left:150px;top:2262px;width:350px;height:458px;background:linear-gradient(180deg,#8d93a0 0%,#a88370 45%,#5b6d8a 100%)}
.coach-kicker{left:580px;top:2312px;font:700 24px "Montserrat",sans-serif;color:var(--ink)}
.coach-brand{left:580px;top:2342px;font:800 46px "Montserrat",sans-serif;color:var(--blue-deep)}
.coach-rule{left:580px;top:2408px;width:480px;height:1px;background:#c3c6cd}
.coach-name{left:580px;top:2424px;font:700 26px "Montserrat",sans-serif;color:var(--ink)}
.coach-spec{left:580px;top:2462px;font-size:14px;color:var(--grey)}
.coach-about{left:580px;top:2506px;font:700 26px "Montserrat",sans-serif;color:var(--ink)}
.coach-copy{left:580px;top:2548px;width:480px;font-size:14px;line-height:1.6;color:var(--grey)}

/* footer */
.footer-nav{left:0;top:2752px;width:1200px;display:flex;justify-content:center;gap:14px;font:600 13px "Montserrat",sans-serif;color:var(--grey)}
.footer-nav .current{color:var(--blue-deep)}
.footer-brand{left:525px;top:2800px;width:150px;text-align:center}
.footer-brand .brand-mark{width:52px;height:52px}
.footer-social{left:530px;top:2908px;display:flex;gap:10px}
.footer-social span{width:26px;height:26px;border-radius:50%;background:var(--blue-deep)}
.copyright{left:0;top:2962px;width:1200px;text-align:center;font-size:12px;color:var(--grey)}
</style>
</head>
<body>

<header>
  <div class="abs utility"></div>
  <div class="abs social"><span></span><span></span><span></span><span></span></div>
  <div class="abs contact-item" style="left:380px">
    <svg viewBox="0 0 24 24"><path d="M6.6 10.8a15 15 0 0 0 6.6 6.6l2.2-2.2c.3-.3.7-.4 1-.2 1.1.4 2.3.6 3.6.6.6 0 1 .4 1 1V20c0 .6-.4 1-1 1A17 17 0 0 1 3 4c0-.6.4-1 1-1h3.5c.6 0 1 .4 1 1 0 1.3.2 2.5.6 3.6.1.3 0 .7-.2 1z"/></svg>
    555 014 2290
  </div>
  <div class="abs contact-item" style="left:560px">
    <svg viewBox="0 0 24 24"><path d="M2 5h20v14H2zm2 2v.5l8 5 8-5V7zm0 2.8V17h16V9.8l-8 5z"/></svg>
    info@craftedember.com
  </div>
  <div class="abs join-top">JOIN NOW</div>

  <div class="abs brand">
    <div class="brand-mark"></div>
    <div class="brand-name">CRAFTED EMBER</div>
  </div>
  <nav class="abs nav">
    <a class="current">HOME</a><a>ABOUT</a><a>SERVICES</a><a>NUTRITION</a><a>TRAINER</a><a>BLOG</a><a>CONTACT</a>
  </nav>
</header>

<section>
  <div class="abs hero-photo" role="img" aria-label="Coach spotting a client doing dumbbell presses on a bench in a gym"></div>
  <div class="abs hero-square"></div>
  <div class="abs welcome">
    <div class="welcome-kicker">WELCOME TO</div>
    <div class="welcome-title">CRAFTED EMBER</div>
    <p class="welcome-copy">Personal coaching that blends smart training and simple nutrition to help you feel stronger, move better and build habits that last. Start today with a plan built around your goals, your schedule and your life.</p>
  </div>
  <div class="abs btn join-hero">JOIN NOW</div>
</section>

<section>
  <div class="abs story"></div>
  <div class="abs story-name">DEREK'S</div>
  <div class="abs story-sub">Awesome Success Story:</div>
  <p class="abs story-copy">Derek came to us tired and stuck. With weekly check-ins, a clear meal plan and steady training he dropped twenty pounds in five months.</p>
  <div class="abs story-result">180 lbs to 160 lbs - Total weight loss = 20 lbs</div>
  <div class="abs btn read-more">Read More</div>

  <div class="abs label-ba" style="left:650px;top:1344px">before</div>
  <svg class="abs" style="left:770px;top:1332px" width="150" height="40" viewBox="0 0 150 40">
    <path d="M10 30 Q75 0 135 26" fill="none" stroke="#85acd3" stroke-width="3"/>
    <path d="M124 18 L137 27 L122 33" fill="none" stroke="#85acd3" stroke-width="3"/>
  </svg>
  <div class="abs label-ba" style="left:958px;top:1344px">after</div>
  <div class="abs ba-frame" style="left:570px" role="img" aria-label="Client torso before the program"></div>
  <div class="abs ba-frame" style="left:830px" role="img" aria-label="Client torso after the program"></div>
  <div class="abs ba-weight" style="left:570px">180 lbs</div>
  <div class="abs ba-weight" style="left:830px">160 lbs</div>
</section>

<section>
  <h2 class="abs services-title">Services Offered</h2>
  <p class="abs services-sub">Choose the coaching style that fits you best, in person or online.</p>
  <div class="abs service" style="left:124px">
    <div class="service-photo" role="img" aria-label="Smiling woman training with dumbbells" style="background:linear-gradient(135deg,#5f8fc4,#d7c2b4)"></div>
    <div class="service-label">PERSONAL TRAINING</div>
  </div>
  <div class="abs service" style="left:372px">
    <div class="service-photo" role="img" aria-label="Woman doing a floor exercise at home" style="background:linear-gradient(135deg,#e6e6e8,#9aa1ab)"></div>
    <div class="service-label">ONLINE COACHING</div>
  </div>
  <div class="abs service" style="left:612px">
    <div class="service-photo" role="img" aria-label="Group fitness class training together" style="background:linear-gradient(135deg,#8a7c74,#3b3f48)"></div>
    <div class="service-label">GROUP TRAINING</div>
  </div>
  <div class="abs service" style="left:852px">
    <div class="service-photo" role="img" aria-label="Athlete stretching on a mat" style="background:linear-gradient(135deg,#c7ccd4,#4a5466)"></div>
    <div class="service-label">BLOG</div>
  </div>
</section>

<section>
  <div class="abs coach"></div>
  <div class="abs coach-photo" role="img" aria-label="Portrait of the primary coach, muscular man in a cap and jeans"></div>
  <div class="abs coach-kicker">PRIMARY COACH</div>
  <div class="abs coach-brand">CRAFTED EMBER</div>
  <div class="abs coach-rule"></div>
  <div class="abs coach-name">NOLAN REYES</div>
  <div class="abs coach-spec">Specialty: Weight Management, Functional Training, Senior Fitness</div>
  <div class="abs coach-about">ABOUT NOLAN REYES</div>
  <p class="abs coach-copy">I have coached clients for over ten years, helping busy people lose weight, gain strength and enjoy food again. My approach is simple: honest guidance, realistic plans and steady support every week until the results stick.</p>
</section>

<footer>
  <div class="abs footer-nav">
    <span class="current">HOME</span><span>|</span><span>ABOUT</span><span>|</span><span>SERVICES</span><span>|</span><span>NUTRITION</span><span>|</span><span>TRAINER</span><span>|</span><span>BLOG</span><span>|</span><span>CONTACT</span>
  </div>
  <div class="abs footer-brand">
    <div class="brand-mark"></div>
    <div class="brand-name">CRAFTED EMBER</div>
  </div>
  <div class="abs footer-social"><span></span><span></span><span></span><span></span></div>
  <div class="abs copyright">Copyright © 2017. All rights reserved.</div>
</footer>

</body>
</html>
```